Whiskey label

I have an existing logo that I currently use for our moonshine and would like to create a similar design for our new whiskey product. We have other products check out our website www.harlowmillstill.com. Looking to release a new product with a similar design label so the public can relate it to our other products but different enough so it stands out from the competition

Target Market(s)

Male and Female 21+

Industry/Entity Type

Product

Logo Text

Dusty Pemberly's Ironside Whiskey

Colors

Designer to choose colors to be used in the design.

Requirements
Must have
• Image of man in chair either photo or something similar to that on our moonshine label. Country theme
Nice to have
• a label design that will stand out from the competition

```html
<!DOCTYPE html>
<html lang="en">
<head>
<meta charset="utf-8">
<title>Dusty Pemberly's Ironside Whiskey Label</title>
<link rel="stylesheet" href="https://fonts.googleapis.com/css2?family=Oswald:wght@600;700&family=Alfa+Slab+One&family=Yellowtail&display=swap">
<style>
  :root {
    --ink: #3b3b3b;
    --ink-soft: #8c8c8c;
    --paper: #ffffff;
    --art-light: #f1f1f1;
    --art-dark: #5a5a5a;
  }
  html, body {
    margin: 0;
    padding: 0;
    width: 1200px;
    height: 600px;
    overflow: hidden;
    background: var(--paper);
  }
  .label {
    display: block;
    width: 1200px;
    height: 600px;
  }
  .brand-arc {
    font-family: "Oswald", sans-serif;
    font-weight: 700;
    font-size: 23px;
    letter-spacing: 1.5px;
    fill: var(--ink);
  }
  .frame-outer { fill: none; stroke: var(--ink); stroke-width: 6; }
  .frame-inner { fill: none; stroke: var(--ink); stroke-width: 1.6; }
  .knockout { fill: var(--paper); }
  .tagline {
    font-family: "Yellowtail", cursive;
    font-size: 22px;
    fill: var(--ink);
  }
  .variety {
    font-family: "Alfa Slab One", serif;
    font-size: 20px;
    letter-spacing: 1px;
    fill: var(--ink);
  }
  .product {
    font-family: "Alfa Slab One", serif;
    font-size: 48px;
    fill: var(--ink);
  }
  .origin {
    font-family: "Oswald", sans-serif;
    font-weight: 700;
    font-size: 9px;
    fill: var(--ink);
  }
  .strength {
    font-family: "Oswald", sans-serif;
    font-weight: 600;
    font-size: 10px;
    letter-spacing: 1.5px;
    fill: var(--ink);
  }
</style>
</head>
<body>
<svg class="label" viewBox="0 0 1200 600" xmlns="http://www.w3.org/2000/svg">
  <defs>
    <path id="brand-curve" d="M488,148 Q560,78 702,92"/>
    <path id="strength-curve" d="M518,462 Q606,502 694,462"/>
    <radialGradient id="portrait-tone" cx="50%" cy="45%" r="60%">
      <stop offset="0%" stop-color="var(--art-dark)"/>
      <stop offset="55%" stop-color="var(--ink-soft)"/>
      <stop offset="100%" stop-color="var(--art-light)"/>
    </radialGradient>
  </defs>

  <text class="brand-arc"><textPath href="#brand-curve">DUSTY PEMBERLY'S</textPath></text>

  <path class="frame-outer" d="M492,152 H636 Q652,152 657,138 Q664,116 690,116 H720 V452 H662 Q606,486 550,452 H492 Z"/>
  <path class="frame-inner" d="M501,161 H640 Q658,161 664,146 Q670,126 690,126 H711 V443 H660 Q606,474 552,443 H501 Z"/>

  <rect class="portrait-art" role="img" aria-label="Illustration of a man seated in a wooden chair holding a bottle, with a sunburst behind him"
        x="556" y="134" width="124" height="198" rx="4" fill="url(#portrait-tone)"/>

  <text class="tagline" x="512" y="357">Authentic</text>
  <text class="variety" x="600" y="380" text-anchor="middle">IRONSIDE</text>

  <rect class="knockout" x="486" y="386" width="240" height="56"/>
  <text class="product" x="606" y="423" text-anchor="middle" textLength="212" lengthAdjust="spacingAndGlyphs">WHISKEY</text>
  <text class="origin" x="606" y="437" text-anchor="middle" textLength="222" lengthAdjust="spacingAndGlyphs">BOTTLED AND DISTILLED IN HARLOW MILL, NORTH CAROLINA</text>

  <text class="strength"><textPath href="#strength-curve" startOffset="50%" text-anchor="middle">50% ALC/ VOL 100 PROOF 750ML</textPath></text>
</svg>
</body>
</html>
```